Stationery Design Project

We need, stationary designs for a store of children and juvenile furniture.
we have the logo. also need tags for the furniture with enought space to include description and options , maybe a 4" x 6" tag.

Target Market(s)

Parents of childrens and teens

Industry/Entity Type

Store

```html
<!DOCTYPE html>
<html lang="en">
<head>
<meta charset="utf-8">
<title>Little Haven – Price Tag</title>
<link rel="stylesheet" href="https://fonts.googleapis.com/css2?family=Open+Sans:wdth,wght@75..100,400..700&display=swap">
<style>
  :root {
    --sky-edge: #55c3cf;
    --sky-centre: #d6eff3;
    --tag-white: #ffffff;
    --cloud-light: #f6f7f8;
    --cloud-grey: #e3e5e8;
    --teal: #55c3cf;
    --orange: #f27a24;
    --rule-grey: #9a9a9a;
    --brand-grey: #7a7a7a;
    --string-brown: #4a3a2a;
    --eyelet: #4b4a2e;
  }

  html, body {
    margin: 0;
    padding: 0;
    overflow: hidden;
  }

  .canvas {
    position: relative;
    width: 1200px;
    height: 900px;
    overflow: hidden;
    background: radial-gradient(ellipse 520px 470px at 600px 470px, var(--sky-centre) 0%, #a7dde4 55%, var(--sky-edge) 100%);
    font-family: "Open Sans", "Arial Narrow", sans-serif;
    font-stretch: 75%;
  }

  .hang-string {
    position: absolute;
    left: 0;
    top: 0;
    width: 1200px;
    height: 900px;
    pointer-events: none;
  }

  .price-tag {
    position: absolute;
    left: 396px;
    top: 258px;
    width: 420px;
    height: 532px;
    background: var(--tag-white);
    border-radius: 18px;
    box-shadow: 3px 5px 8px rgba(0, 60, 70, 0.22);
  }

  .cloud-crown {
    position: absolute;
    left: 396px;
    top: 180px;
    width: 420px;
    height: 165px;
    border-radius: 80px 90px 30px 30px;
    background: radial-gradient(ellipse at 50% 45%, var(--cloud-light) 0%, var(--cloud-light) 55%, var(--cloud-grey) 100%);
  }

  .eyelet {
    position: absolute;
    left: 591px;
    top: 222px;
    width: 24px;
    height: 24px;
  }

  .item-name {
    position: absolute;
    left: 396px;
    top: 392px;
    width: 420px;
    margin: 0;
    text-align: center;
    font-size: 35px;
    font-weight: 700;
    letter-spacing: 0.5px;
    color: var(--teal);
    line-height: 1;
  }

  .divider {
    position: absolute;
    left: 484px;
    width: 244px;
    height: 0;
    border-top: 1.5px solid var(--rule-grey);
  }
  .divider--top { top: 456px; }
  .divider--bottom { top: 596px; }

  .price {
    position: absolute;
    left: 518px;
    top: 470px;
    height: 110px;
    color: var(--orange);
    font-weight: 700;
    line-height: 1;
  }
  .price__currency {
    position: absolute;
    left: 0;
    top: 18px;
    font-size: 58px;
  }
  .price__whole {
    position: absolute;
    left: 28px;
    top: -2px;
    font-size: 118px;
    letter-spacing: -2px;
  }
  .price__cents {
    position: absolute;
    left: 136px;
    top: 14px;
    font-size: 36px;
    padding: 0 2px 4px;
    border-bottom: 1.5px solid var(--rule-grey);
  }

  .brand-name {
    position: absolute;
    left: 396px;
    top: 706px;
    width: 420px;
    margin: 0;
    text-align: center;
    font-size: 34px;
    font-weight: 600;
    letter-spacing: 1px;
    color: var(--brand-grey);
    line-height: 1;
  }
</style>
</head>
<body>
  <main class="canvas">
    <div class="price-tag"></div>
    <div class="cloud-crown" role="img" aria-label="Soft white cloud illustration crowning the top of the tag"></div>

    <svg class="hang-string" viewBox="0 0 1200 900" aria-hidden="true">
      <path d="M603 230 C 598 180, 640 100, 700 68 C 745 45, 772 62, 758 95 C 740 135, 650 150, 606 228"
            fill="none" stroke="var(--string-brown)" stroke-width="3" stroke-linecap="round"/>
    </svg>

    <svg class="eyelet" viewBox="0 0 24 24" aria-hidden="true">
      <circle cx="12" cy="12" r="10" fill="var(--eyelet)"/>
      <circle cx="12" cy="12" r="5" fill="var(--tag-white)"/>
    </svg>

    <h1 class="item-name">ITEM NAME</h1>
    <div class="divider divider--top"></div>

    <p class="price" aria-label="Price 49 dollars 99 cents">
      <span class="price__currency">$</span>
      <span class="price__whole">49</span>
      <span class="price__cents">99</span>
    </p>

    <div class="divider divider--bottom"></div>

    <p class="brand-name">Little Haven</p>
  </main>
</body>
</html>
```